Bespoke Branding Agency "Tidal Marks" seeks uplifting wordpress site

Looking for a SIMPLE, CLEAN, easy to manage wordpress site for our start-up Branding business. Our company is "Tidal Marks" and the site should reflect our vision.

We formed the company after making the decision never to work the average 9 to 5 work life again. We have vowed to never work in traditional corporate culture again. We are committed to a happier life with reduced stress and increased job satisfaction.

We want to build brands that make people happy.

We want to work with people who believe that you don’t have to be an asshole to be successful.

We believe that success should not be measured in monetary terms, but rather in happiness scores.

We believe in the Corwin Ashdale song lyric "Folks ought to grin often”.

We love sunflowers.

We prefer brevity over long wind.

We are motivated by creativity not money.

We love spending time with friends and family, and see this as our main priority in life.

We know life is short.

Industry/Entity Type

Business

```html
<!DOCTYPE html>
<html lang="en">
<head>
<meta charset="utf-8">
<title>Tidal Marks</title>
<link href="https://fonts.googleapis.com/css2?family=Oswald:wght@400&family=Roboto:wght@400&family=Raleway:wght@500&display=swap" rel="stylesheet">
<style>
  :root {
    --brand: #ec1459;
    --ink: #333333;
    --white: #ffffff;
    --footer: #1c1c1c;
    --panel: rgba(120, 120, 120, 0.55);
    --band: rgba(60, 60, 60, 0.75);
    --social: #3a9ad9;
  }
  * { margin: 0; padding: 0; box-sizing: border-box; }
  html, body { width: 1200px; height: 1051px; overflow: hidden; background: var(--white); }
  body { position: relative; font-family: "Roboto", sans-serif; }

  .site-header { position: absolute; top: 0; left: 0; width: 1200px; height: 114px; background: var(--white); z-index: 3; }
  .main-nav a {
    position: absolute; top: 60px; font-size: 16px; color: var(--ink);
    text-decoration: none; text-transform: uppercase; letter-spacing: 0.2px;
  }
  .main-nav a.is-active { color: var(--brand); }

  .brand-badge {
    position: absolute; left: 520px; top: 15px; width: 162px; height: 162px; border-radius: 50%;
    background: var(--brand); color: var(--white); z-index: 4;
    display: flex; flex-direction: column; align-items: center; justify-content: center;
    text-align: center; white-space: nowrap;
    font-family: "Raleway", sans-serif; font-weight: 500; font-size: 24px; line-height: 28px;
    letter-spacing: 3px; text-transform: uppercase;
  }
  .brand-badge span { display: block; padding-left: 3px; }

  .hero {
    position: absolute; top: 114px; left: 0; width: 1200px; height: 821px;
    background:
      radial-gradient(ellipse 260px 340px at 930px 420px, rgba(110, 60, 40, 0.35), transparent 70%),
      radial-gradient(ellipse 700px 400px at 500px 300px, #e8d640, transparent 75%),
      linear-gradient(180deg, #c7cf6a 0%, #b9c24a 35%, #9fae3a 65%, #6f8a35 100%);
  }
  .hero-title {
    position: absolute; left: 88px; top: 340px; z-index: 2;
    font-family: "Oswald", sans-serif; font-weight: 400; font-size: 66px; line-height: 76px;
    color: var(--white); text-transform: uppercase; letter-spacing: -1px;
  }
  .slider-controls { position: absolute; left: 92px; top: 509px; display: flex; gap: 2px; z-index: 2; }
  .slider-controls span { width: 41px; height: 53px; background: rgba(20, 20, 20, 0.85); display: flex; align-items: center; justify-content: center; }

  .feature-band { position: absolute; left: 0; top: 734px; width: 1200px; height: 201px; background: var(--band); z-index: 1; }
  .feature {
    position: absolute; top: 734px; width: 336px; height: 201px; background: var(--panel); z-index: 2;
    text-align: center; color: var(--white);
  }
  .feature-icon {
    position: absolute; left: 50%; top: -61px; width: 106px; height: 106px; margin-left: -53px; border-radius: 50%;
    background: var(--brand); border: 3px solid var(--white);
    display: flex; align-items: center; justify-content: center;
  }
  .feature h2 { margin-top: 66px; font-family: "Raleway", sans-serif; font-weight: 500; font-size: 19px; text-transform: uppercase; }
  .feature p { margin: 16px auto 0; width: 270px; font-size: 13px; line-height: 20px; }

  .site-footer { position: absolute; top: 935px; left: 0; width: 1200px; height: 116px; background: var(--footer); color: var(--white); }
  .footer-links { position: absolute; left: 92px; top: 30px; font-size: 13px; }
  .footer-links a { color: var(--white); text-decoration: none; }
  .footer-links .sep { margin: 0 7px; }
  .copyright { position: absolute; left: 93px; top: 54px; font-size: 13px; }
  .social { position: absolute; top: 38px; display: flex; gap: 21px; left: 944px; }
  .social span { width: 41px; height: 41px; border-radius: 50%; background: var(--social); border: 3px solid #e8e8e8; box-shadow: 0 2px 3px rgba(0,0,0,0.6); }
</style>
</head>
<body>
  <header class="site-header">
    <nav class="main-nav">
      <a class="is-active" style="left:121px">Home</a>
      <a style="left:237px">About Us</a>
      <a style="left:383px">Services</a>
      <a style="left:739px">Brands</a>
      <a style="left:868px">News</a>
      <a style="left:978px">Contacts</a>
    </nav>
  </header>
  <div class="brand-badge"><span>Tidal</span><span>Marks</span></div>

  <section class="hero" role="img" aria-label="Photo of a smiling woman among a field of sunflowers"></section>
  <h1 class="hero-title">Folks ought to<br>grin often</h1>
  <div class="slider-controls">
    <span><svg width="14" height="28" viewBox="0 0 14 28"><path d="M12 2 L2 14 L12 26" fill="none" stroke="#fff" stroke-width="1.5"/></svg></span>
    <span><svg width="14" height="28" viewBox="0 0 14 28"><path d="M2 2 L12 14 L2 26" fill="none" stroke="#fff" stroke-width="1.5"/></svg></span>
  </div>

  <div class="feature-band"></div>
  <article class="feature" style="left:87px">
    <div class="feature-icon">
      <svg width="34" height="38" viewBox="0 0 34 38"><circle cx="17" cy="10" r="9" fill="#fff"/><path d="M2 37 C2 24 8 21 17 21 C26 21 32 24 32 37 Z" fill="#fff"/></svg>
    </div>
    <h2>About Us</h2>
    <p>Lorem Ipsum has been the industry’s standard dummy text ever since the 1500s, when an unknown printer took a galley of type</p>
  </article>
  <article class="feature" style="left:433px">
    <div class="feature-icon">
      <svg width="42" height="40" viewBox="0 0 42 40"><path d="M41 1 L1 18 L13 23 L35 7 L17 26 L19 39 L25 29 L33 33 Z" fill="#fff"/></svg>
    </div>
    <h2>What We Do</h2>
    <p>Lorem Ipsum has been the industry’s standard dummy text ever since the 1500s, when an unknown printer took a galley of type</p>
  </article>
  <article class="feature" style="left:777px">
    <div class="feature-icon">
      <svg width="44" height="40" viewBox="0 0 44 40"><circle cx="8" cy="9" r="6" fill="#fff"/><circle cx="36" cy="9" r="6" fill="#fff"/><circle cx="22" cy="12" r="8" fill="#fff"/><path d="M0 28 C0 19 4 17 9 17 C13 17 15 18 15 20 L15 28 Z M44 28 C44 19 40 17 35 17 C31 17 29 18 29 20 L29 28 Z" fill="#fff"/><path d="M9 40 C9 26 14 22 22 22 C30 22 35 26 35 40 Z" fill="#fff"/></svg>
    </div>
    <h2>Tidal Marks</h2>
    <p>Lorem Ipsum has been the industry’s standard dummy text ever since the 1500s, when an unknown printer took a galley of type</p>
  </article>

  <footer class="site-footer">
    <div class="footer-links">
      <a>Privacy Policy</a><span class="sep">|</span><a>Terms of Use</a><span class="sep">|</span><a>About Us</a><span class="sep">|</span><a>Sitemap</a>
    </div>
    <div class="copyright">Copyright © 2015&nbsp; All Rights</div>
    <div class="social"><span></span><span></span><span></span></div>
  </footer>
</body>
</html>
```